a residential painting contractor I need a 6x9 postcard made

I already have a logo, I'm trying to offer my services to people. you can put that there's a 250$ discount for first time customers. include my License number #4629318 as well as the services I offer, interior and exterior painting, pressure washing, cabinet painting, epoxy floors, wood staining, decks, fences and much more. I'm licensed bonded and insured as well.

Target Market(s)

residential consumers (homeowners)

Industry/Entity Type

Painting contractor

Requirements
Must have
• postage stuff on the back I've linked some pictures top right please, my license number, what I do, phone number (341)572-6190 email brushkelvo7@maplint.com, front and back of postcard
Nice to have
• well lit house in the background, maybe little circles of people doing some of the services I offer

```html
<!DOCTYPE html>
<html lang="en">
<head>
<meta charset="utf-8">
<title>Kelvo Painting – Postcard Front and Back</title>
<link rel="stylesheet" href="https://fonts.googleapis.com/css2?family=Oswald:wght@500;600&family=Lato:wght@400;700;900&display=swap">
<style>
  :root{
    --stage:#3b3b44;
    --navy:#1f1f4d;
    --navy-mid:#4a4a8a;
    --band:#5b5b9e;
    --lavender:#a9a9e0;
    --lavender-soft:#a6a6d6;
    --gold:#f5a623;
    --orange:#f8ad33;
    --ring:#f9c842;
    --maroon:#8e1538;
    --check:#b01e3c;
    --white:#ffffff;
  }
  *{margin:0;padding:0;box-sizing:border-box}
  html,body{width:1200px;height:1200px;overflow:hidden;background:var(--stage)}
  body{position:relative;font-family:"Lato",Arial,sans-serif}
  .card{position:absolute;left:209px;width:818px;overflow:hidden;background:var(--white)}
  .card--front{top:46px;height:544px}
  .card--back{top:612px;height:547px}
  .card svg.bg{position:absolute;left:0;top:0}
  .abs{position:absolute;white-space:nowrap}

  /* front */
  .title{left:22px;top:26px;font-family:"Oswald",sans-serif;font-weight:600;font-size:60px;line-height:1;color:var(--white)}
  .title span{color:var(--lavender)}
  .credentials{left:24px;top:102px;font-size:20px;color:var(--white);letter-spacing:.5px}
  .license-front{left:24px;top:130px;font-size:17px;color:var(--gold);letter-spacing:.5px}
  .services{left:26px;top:196px;list-style:none}
  .services li{display:flex;align-items:center;height:21px;font-size:18px;color:var(--navy);letter-spacing:.3px}
  .services svg{width:14px;height:14px;margin-right:12px}
  .discount{left:19px;top:363px;width:164px;height:164px;border-radius:50%;background:var(--maroon);border:5px solid var(--white);
    display:flex;flex-direction:column;align-items:center;justify-content:center;color:var(--white)}
  .discount__amount{font-family:"Oswald",sans-serif;font-weight:600;font-size:58px;line-height:1;color:var(--gold)}
  .discount__label{font-size:21px;letter-spacing:.5px;margin-top:4px}
  .first-time{left:190px;top:472px;font-size:20px;line-height:24px;color:var(--white)}
  .brand-seal{border-radius:50%;background:var(--white);display:flex;align-items:center;justify-content:center;text-align:center;
    font-family:"Oswald",sans-serif;font-weight:600;color:var(--navy);line-height:1.05}
  .front-seal{left:327px;top:321px;width:212px;height:212px;border:10px solid var(--navy-mid);box-shadow:inset 0 0 0 5px var(--gold);font-size:30px}
  .call-badge{left:748px;top:395px;width:54px;height:54px;border-radius:50%;background:var(--navy);display:flex;align-items:center;justify-content:center}
  .phone-front{right:16px;top:466px;font-family:"Oswald",sans-serif;font-weight:500;font-size:31px;color:var(--navy)}
  .email-front{right:16px;top:507px;font-size:20px;color:var(--navy);display:flex;align-items:center;gap:8px}

  /* back */
  .back-seal{left:19px;top:12px;width:192px;height:192px;border:10px solid var(--navy-mid);box-shadow:inset 0 0 0 5px var(--gold);font-size:29px}
  .service-photo{border-radius:50%;border:7px solid var(--ring);box-shadow:0 0 0 5px var(--white)}
  .photo-washing{left:250px;top:132px;width:168px;height:168px;background:radial-gradient(circle at 40% 60%,#d7b13a,#7c8797 55%,#b5bcc6)}
  .photo-staining{left:371px;top:252px;width:168px;height:168px;background:linear-gradient(100deg,#c99a62,#e4bd8a 45%,#5d8fd6 60%,#c69560)}
  .service-heading{left:18px;top:262px;font-weight:900;font-size:24px;line-height:30px;color:var(--navy)}
  .service-copy{left:18px;top:326px;width:305px;white-space:normal;font-size:14.5px;line-height:17.5px;color:var(--navy)}
  .license-back{left:18px;top:430px;font-weight:700;font-size:18px;color:var(--navy);letter-spacing:.3px}
  .postage{left:680px;top:28px;width:107px;height:80px;border:1.5px solid #444;font-family:Arial,sans-serif;font-weight:700;font-size:11px;
    line-height:14.5px;text-align:center;padding-top:4px;color:#111}
  .postage b{font-size:12.5px}
  .address-box{left:562px;top:139px;width:225px;height:54px;border:1.5px solid #333;font-family:Arial,sans-serif;font-weight:700;font-size:14px;
    line-height:17px;padding:8px 14px;color:#111}
  .footer-bar{left:0;top:463px;width:818px;height:84px;background:var(--band)}
  .footer-name{left:25px;top:489px;font-family:"Oswald",sans-serif;font-weight:500;font-size:23px;color:var(--white)}
  .footer-icon{width:62px;height:62px;border-radius:50%;background:var(--navy);border:3px solid var(--white);display:flex;align-items:center;justify-content:center}
  .footer-icon--phone{left:196px;top:474px}
  .footer-icon--mail{left:473px;top:474px}
  .footer-phone{left:276px;top:484px;font-family:"Oswald",sans-serif;font-weight:500;font-size:31px;color:var(--white)}
  .footer-email{left:543px;top:491px;font-size:22px;color:var(--white)}
</style>
</head>
<body>

<section class="card card--front" aria-label="Postcard front">
  <svg class="bg" width="818" height="544" viewBox="0 0 818 544">
    <defs>
      <linearGradient id="lavFill" x1="0" y1="0" x2="0" y2="1">
        <stop offset="0" stop-color="#b3b3e2"/>
        <stop offset="1" stop-color="#8181c0"/>
      </linearGradient>
      <linearGradient id="houseScene" x1="0" y1="0" x2="0" y2="1">
        <stop offset="0" stop-color="#8b8fc4"/>
        <stop offset=".35" stop-color="#c9b5c9"/>
        <stop offset=".6" stop-color="#6d7191"/>
        <stop offset=".85" stop-color="#5f6a6a"/>
        <stop offset="1" stop-color="#7c8676"/>
      </linearGradient>
    </defs>
    <rect width="818" height="544" fill="url(#lavFill)"/>
    <rect width="460" height="176" fill="var(--navy)"/>
    <path d="M0,420 C140,360 300,360 480,400 L480,544 L0,544 Z" fill="var(--navy)"/>
    <path d="M0,438 C140,380 300,380 480,416" fill="none" stroke="var(--navy-mid)" stroke-width="6"/>
    <path role="img" aria-label="Photo of a well-lit two-storey house with garage at dusk"
      d="M460,0 L818,0 L818,410 C700,430 560,470 455,544 L420,544 C380,400 370,160 460,0 Z" fill="url(#houseScene)"/>
    <path d="M460,0 C370,160 380,400 420,544" fill="none" stroke="var(--white)" stroke-width="8"/>
    <path d="M818,400 C690,420 560,468 440,544 L818,544 Z" fill="var(--lavender-soft)"/>
    <path d="M818,400 C690,420 560,468 440,544" fill="none" stroke="var(--white)" stroke-width="7"/>
  </svg>

  <h1 class="abs title">KELVO <span>PAINTING</span></h1>
  <p class="abs credentials">LICENSED, BONDED &amp; INSURED</p>
  <p class="abs license-front">LICENSE NUMBER #4629318</p>

  <ul class="abs services">
    <li><svg viewBox="0 0 14 14"><path d="M1,7 L5,12 L13,1" fill="none" stroke="var(--check)" stroke-width="2"/></svg>INTERIOR &amp; EXTERIOR PAINTING</li>
    <li><svg viewBox="0 0 14 14"><path d="M1,7 L5,12 L13,1" fill="none" stroke="var(--check)" stroke-width="2"/></svg>PRESSURE WASHING</li>
    <li><svg viewBox="0 0 14 14"><path d="M1,7 L5,12 L13,1" fill="none" stroke="var(--check)" stroke-width="2"/></svg>CABINET PAINTING</li>
    <li><svg viewBox="0 0 14 14"><path d="M1,7 L5,12 L13,1" fill="none" stroke="var(--check)" stroke-width="2"/></svg>EPOXY FLOORS</li>
    <li><svg viewBox="0 0 14 14"><path d="M1,7 L5,12 L13,1" fill="none" stroke="var(--check)" stroke-width="2"/></svg>WOOD STAINING DECKS</li>
    <li><svg viewBox="0 0 14 14"><path d="M1,7 L5,12 L13,1" fill="none" stroke="var(--check)" stroke-width="2"/></svg>FENCES</li>
    <li><svg viewBox="0 0 14 14"><path d="M1,7 L5,12 L13,1" fill="none" stroke="var(--check)" stroke-width="2"/></svg>AND MUCH MORE</li>
  </ul>

  <div class="abs discount">
    <span class="discount__amount">$250</span>
    <span class="discount__label">DISCOUNT</span>
  </div>
  <p class="abs first-time">For 1st Time<br>Customer!</p>

  <div class="abs brand-seal front-seal">KELVO<br>PAINTING</div>

  <div class="abs call-badge">
    <svg width="26" height="26" viewBox="0 0 24 24"><path d="M6.6,10.8a15.2,15.2,0,0,0,6.6,6.6l2.2-2.2a1,1,0,0,1,1-.25,11.4,11.4,0,0,0,3.6.57,1,1,0,0,1,1,1V20a1,1,0,0,1-1,1A17,17,0,0,1,3,4,1,1,0,0,1,4,3H7.5a1,1,0,0,1,1,1,11.4,11.4,0,0,0,.57,3.6,1,1,0,0,1-.25,1Z" fill="var(--gold)"/></svg>
  </div>
  <p class="abs phone-front">(341)572-6190</p>
  <p class="abs email-front">
    <svg width="22" height="16" viewBox="0 0 22 16"><rect width="22" height="16" rx="1.5" fill="var(--navy)"/><path d="M1,1 L11,9 L21,1" fill="none" stroke="var(--lavender-soft)" stroke-width="1.6"/></svg>
    brushkelvo7@maplint.com
  </p>
</section>

<section class="card card--back" aria-label="Postcard back">
  <svg class="bg" width="818" height="547" viewBox="0 0 818 547">
    <path d="M0,104 C120,60 250,40 360,52 C470,110 560,300 548,463 L0,463 Z" fill="var(--navy)"/>
    <path d="M0,120 C120,80 250,62 352,72 C455,130 540,310 530,463 L0,463 Z" fill="var(--orange)"/>
  </svg>

  <div class="abs brand-seal back-seal">KELVO<br>PAINTING</div>

  <div class="abs service-photo photo-washing" role="img" aria-label="Photo of a worker pressure washing house siding"></div>
  <div class="abs service-photo photo-staining" role="img" aria-label="Photo of a brush applying blue paint to wood"></div>

  <h2 class="abs service-heading">WE PROVIDE<br>THE BEST SERVICE</h2>
  <p class="abs service-copy">Lorem ipsum dolor sit amet, consectetur adipiscing elit. Sed volutpat pretium pharetra. Maecenas porta diam justo, vitae hendrerit nisi commodo et.</p>
  <p class="abs license-back">LICENSE NUMBER #4629318</p>

  <div class="abs postage">PRSRT STD<br>ECRWSS<br>U.S.POSTAGE<br><b>PAID</b><br>EDDM Retail</div>
  <div class="abs address-box">LOCAL POSTAL<br>CUSTOMER</div>

  <div class="abs footer-bar"></div>
  <p class="abs footer-name">KELVO PAINTING</p>
  <div class="abs footer-icon footer-icon--phone">
    <svg width="28" height="28" viewBox="0 0 24 24"><path d="M6.6,10.8a15.2,15.2,0,0,0,6.6,6.6l2.2-2.2a1,1,0,0,1,1-.25,11.4,11.4,0,0,0,3.6.57,1,1,0,0,1,1,1V20a1,1,0,0,1-1,1A17,17,0,0,1,3,4,1,1,0,0,1,4,3H7.5a1,1,0,0,1,1,1,11.4,11.4,0,0,0,.57,3.6,1,1,0,0,1-.25,1Z" fill="var(--gold)"/></svg>
  </div>
  <p class="abs footer-phone">(341)572-6190</p>
  <div class="abs footer-icon footer-icon--mail">
    <svg width="28" height="20" viewBox="0 0 22 16"><rect width="22" height="16" rx="1.5" fill="var(--gold)"/><path d="M1,1 L11,9 L21,1" fill="none" stroke="var(--navy)" stroke-width="1.6"/></svg>
  </div>
  <p class="abs footer-email">brushkelvo7@maplint.com</p>
</section>

</body>
</html>
```